Brookmere Osteopathy flyer

I want a clean clear DL flyer (but also want an A4 poster) promoting a new Osteopathic business in a semi rural area in Tasmania (Australia).
It can have pictures like the examples attached to show people what Osteopathy is (its like Chiropractic and physiotherapy).
I am the sole practioner and am male, so any pictures would be best to be a white male if possible.
I've attached some wording, you can use all, or none of it
I don't have a phone number for the business yet
info@brookmereosteopathy.example
www.brookmereosteopathy.example
Target Market(s)
Australians, from tradies, professionals, babies to retired people
Industry/Entity Type
Health
Look and feel

```html
<!DOCTYPE html>
<html lang="en">
<head>
<meta charset="utf-8">
<title>Brookmere Osteopathy – DL Flyer</title>
<link rel="stylesheet" href="https://fonts.googleapis.com/css2?family=Mulish:wght@400;600;700&family=Saira+Extra+Condensed:wght@600;700&family=Josefin+Slab:wght@600&display=swap">
<style>
  :root {
    --brand-blue: #1b8bcc;
    --heading-blue: #1a87cf;
    --accent-orange: #f39a2e;
    --ink: #232323;
    --paper: #ffffff;
    --backdrop: #e9e9e9;
    --arc-dark: #2a2a2a;
  }
  * { margin: 0; padding: 0; box-sizing: border-box; }
  html, body { width: 1161px; height: 1200px; overflow: hidden; }
  body {
    background: var(--backdrop);
    font-family: "Mulish", sans-serif;
    color: var(--ink);
    position: relative;
  }
  .flyer-side {
    position: absolute;
    top: 107px;
    width: 462px;
    height: 984px;
    background: var(--paper);
    overflow: hidden;
    box-shadow: 0 2px 8px rgba(0,0,0,.15);
  }
  .flyer-front { left: 100px; }
  .flyer-back { left: 597px; }

  /* Brand name in place of a logo */
  .brand-mark {
    position: absolute;
    display: flex;
    align-items: center;
    gap: 8px;
    font-family: "Mulish", sans-serif;
    font-weight: 700;
    line-height: 1.15;
  }
  .brand-mark .brand-dot {
    width: 14px; height: 14px; border-radius: 50%;
    flex: none;
  }
  .brand-header { left: 17px; top: 36px; width: 150px; font-size: 15px; color: var(--brand-blue); }
  .brand-header .brand-dot { background: var(--accent-orange); }
  .brand-footer { font-size: 13px; color: var(--paper); width: 110px; }
  .brand-footer .brand-dot { background: var(--paper); }

  /* Call-to-action phone block */
  .call-block { position: absolute; display: flex; align-items: center; }
  .call-block .phone-icon { width: 38px; height: 44px; flex: none; }
  .call-label { font-size: 15.5px; font-weight: 600; letter-spacing: .2px; }
  .call-number {
    font-family: "Josefin Slab", serif;
    font-size: 34px; font-weight: 600; line-height: 1;
    margin-top: 4px;
  }
  .call-header { left: 194px; top: 30px; gap: 14px; color: var(--heading-blue); }
  .call-footer { left: 15px; top: 908px; gap: 12px; color: var(--paper); }

  /* Photo areas */
  .photo-area { position: absolute; left: 0; display: block; }
  .front-photo { top: 108px; }
  .back-photo { top: 0; }

  .service-title {
    position: absolute; left: 21px; top: 236px;
    font-family: "Saira Extra Condensed", sans-serif;
    font-weight: 700;
    font-size: 47px;
    line-height: 53px;
    letter-spacing: .8px;
    color: var(--heading-blue);
    text-shadow: 0 0 2px #fff, 0 0 1px #fff;
  }

  .intro-copy {
    position: absolute; left: 14px; top: 606px; width: 440px;
    font-size: 15.6px; line-height: 34px; color: var(--ink);
  }
  .service-area {
    position: absolute; left: 14px; top: 778px;
    font-size: 16.8px; font-weight: 700; letter-spacing: .2px;
  }
  .offer {
    position: absolute; left: 14px; top: 800px;
    font-family: "Saira Extra Condensed", sans-serif;
    font-weight: 700; font-size: 37px; letter-spacing: .5px;
    color: var(--heading-blue);
  }

  .footer-rule { position: absolute; left: 0; top: 881px; width: 100%; height: 2px; }
  .front-rule { background: var(--accent-orange); }
  .back-rule { background: var(--brand-blue); }
  .footer-band {
    position: absolute; left: 0; top: 888px; width: 100%; height: 96px;
    background: var(--brand-blue);
  }
  .contact-list {
    position: absolute; left: 16px; top: 897px;
    list-style: none; color: var(--paper);
    font-size: 11.3px; font-weight: 700;
  }
  .contact-list li { display: flex; align-items: center; gap: 8px; height: 21.4px; }
  .contact-list svg { width: 11px; height: 11px; flex: none; }
  .front-footer-brand { left: 350px; top: 918px; }
  .back-footer-brand { left: 345px; top: 918px; }

  .reasons-title {
    position: absolute; left: 22px; top: 330px;
    font-size: 30.5px; font-weight: 700; line-height: 37px;
    color: var(--heading-blue);
  }
  .reasons-list {
    position: absolute; left: 22px; top: 420px; list-style: none;
  }
  .reasons-list li {
    display: flex; align-items: center; gap: 13px;
    height: 44.2px; font-size: 20.6px; font-weight: 600; color: var(--ink);
  }
  .reasons-list svg { width: 18px; height: 12px; flex: none; }
</style>
</head>
<body>

<!-- Front of flyer -->
<section class="flyer-side flyer-front">
  <div class="brand-mark brand-header"><span class="brand-dot"></span><span>Brookmere Osteopathy</span></div>

  <div class="call-block call-header">
    <svg class="phone-icon" viewBox="0 0 38 44" fill="none" stroke="var(--accent-orange)" stroke-width="2.2" stroke-linecap="round" stroke-linejoin="round">
      <path d="M8 6 L14 4 L18 15 L13 18 Q16 28 23 33 L28 29 L35 37 L30 41 Q16 42 8 26 Q3 14 8 6 Z"/>
      <path d="M22 9 Q28 11 29 18"/><path d="M23 3 Q33 6 35 17"/>
    </svg>
    <div>
      <div class="call-label">Visit Us Today</div>
      <div class="call-number">555.010.2040</div>
    </div>
  </div>

  <svg class="photo-area front-photo" width="462" height="480" viewBox="0 0 462 480" role="img" aria-label="Photo: practitioner's hands treating a patient's shoulder on a massage table">
    <defs>
      <linearGradient id="frontTone" x1="0" y1="0" x2="1" y2="1">
        <stop offset="0" stop-color="#f0e7e1"/>
        <stop offset="0.45" stop-color="#d8a383"/>
        <stop offset="0.8" stop-color="#c88d6c"/>
        <stop offset="1" stop-color="#eef0f2"/>
      </linearGradient>
    </defs>
    <path d="M0 0 H462 V404 Q231 534 0 404 Z" fill="url(#frontTone)"/>
    <path d="M0 406 Q231 540 462 406" fill="none" stroke="var(--arc-dark)" stroke-width="5"/>
  </svg>

  <h1 class="service-title">CHIROPRACTIC<br>AND<br>PHYSIOTHERAPY</h1>

  <p class="intro-copy">Osteopaths Use A Combination of Joint Manipulation, Targeted Deep Tissue Massage And Stretching To Improve Function, Relieve Pain And Support The Body’s Ability To Heal Itself.</p>

  <p class="service-area">Serving Semi Rural Area In Tasmania - Australia</p>
  <p class="offer">FREE INTIAL PHYSIO CONSULTATION</p>

  <div class="footer-rule front-rule"></div>
  <div class="footer-band"></div>
  <ul class="contact-list">
    <li><svg viewBox="0 0 12 12"><path d="M6 11.5 C3 8 2 6 2 4.2 A4 4 0 0 1 10 4.2 C10 6 9 8 6 11.5 Z" fill="var(--accent-orange)"/><circle cx="6" cy="4.3" r="1.5" fill="var(--brand-blue)"/></svg>48 Willow Creek Road, Brookmere</li>
    <li><svg viewBox="0 0 12 12" fill="none" stroke="var(--accent-orange)" stroke-width="1.2"><circle cx="6" cy="6" r="5.2"/><path d="M4 3.5 L5.2 3 L6 5 L5.2 5.7 Q5.8 7 7 7.6 L7.8 6.9 L9 8 L8.2 8.9 Q5 8.8 4 5.5 Z" fill="var(--accent-orange)" stroke="none"/></svg>555-010-7731</li>
    <li><svg viewBox="0 0 12 12"><path d="M1 5 L6 2 L11 5 V10.5 H1 Z" fill="var(--accent-orange)"/><path d="M1 5 L6 8 L11 5" fill="none" stroke="var(--brand-blue)" stroke-width="1"/></svg>info@brookmereosteopathy.example</li>
    <li><svg viewBox="0 0 12 12" fill="none" stroke="var(--accent-orange)" stroke-width="1"><circle cx="6" cy="6" r="5"/><ellipse cx="6" cy="6" rx="2.2" ry="5"/><path d="M1 6 H11 M2 3.5 H10 M2 8.5 H10"/></svg>www.brookmereosteopathy.example</li>
  </ul>
  <div class="brand-mark brand-footer front-footer-brand"><span class="brand-dot"></span><span>Brookmere Osteopathy</span></div>
</section>

<!-- Back of flyer -->
<section class="flyer-side flyer-back">
  <svg class="photo-area back-photo" width="463" height="330" viewBox="0 0 463 330" role="img" aria-label="Photo: practitioner working on the lower back of a patient lying on their side">
    <defs>
      <linearGradient id="backTone" x1="0" y1="0" x2="1" y2="1">
        <stop offset="0" stop-color="#e9e9ea"/>
        <stop offset="0.35" stop-color="#2e3b5c"/>
        <stop offset="0.55" stop-color="#d7a488"/>
        <stop offset="0.85" stop-color="#c98e70"/>
        <stop offset="1" stop-color="#ececeb"/>
      </linearGradient>
    </defs>
    <path d="M0 0 H463 V257 Q231 385 0 257 Z" fill="url(#backTone)"/>
    <path d="M0 260 Q231 392 463 260" fill="none" stroke="var(--accent-orange)" stroke-width="4"/>
  </svg>

  <h2 class="reasons-title">Common Reasons People<br>Visit An Osteopath:</h2>

  <ul class="reasons-list">
    <li><svg viewBox="0 0 18 12"><path d="M1 11 Q3 4 12 4 V1 L17 5.5 L12 10 V7 Q5 7 1 11 Z" fill="var(--accent-orange)"/></svg>Back / Neck Pain</li>
    <li><svg viewBox="0 0 18 12"><path d="M1 11 Q3 4 12 4 V1 L17 5.5 L12 10 V7 Q5 7 1 11 Z" fill="var(--accent-orange)"/></svg>Headaches / Migraines</li>
    <li><svg viewBox="0 0 18 12"><path d="M1 11 Q3 4 12 4 V1 L17 5.5 L12 10 V7 Q5 7 1 11 Z" fill="var(--accent-orange)"/></svg>Joint And Muscle Pain</li>
    <li><svg viewBox="0 0 18 12"><path d="M1 11 Q3 4 12 4 V1 L17 5.5 L12 10 V7 Q5 7 1 11 Z" fill="var(--accent-orange)"/></svg>Pregnancy-related Discomfort</li>
    <li><svg viewBox="0 0 18 12"><path d="M1 11 Q3 4 12 4 V1 L17 5.5 L12 10 V7 Q5 7 1 11 Z" fill="var(--accent-orange)"/></svg>Disc Related Issues</li>
    <li><svg viewBox="0 0 18 12"><path d="M1 11 Q3 4 12 4 V1 L17 5.5 L12 10 V7 Q5 7 1 11 Z" fill="var(--accent-orange)"/></svg>Sciatica</li>
    <li><svg viewBox="0 0 18 12"><path d="M1 11 Q3 4 12 4 V1 L17 5.5 L12 10 V7 Q5 7 1 11 Z" fill="var(--accent-orange)"/></svg>Plantar Fasciitis</li>
    <li><svg viewBox="0 0 18 12"><path d="M1 11 Q3 4 12 4 V1 L17 5.5 L12 10 V7 Q5 7 1 11 Z" fill="var(--accent-orange)"/></svg>Tendonitis / Bursitis</li>
    <li><svg viewBox="0 0 18 12"><path d="M1 11 Q3 4 12 4 V1 L17 5.5 L12 10 V7 Q5 7 1 11 Z" fill="var(--accent-orange)"/></svg>Adhesive Capsulitis (Frozen Shoulder)</li>
    <li><svg viewBox="0 0 18 12"><path d="M1 11 Q3 4 12 4 V1 L17 5.5 L12 10 V7 Q5 7 1 11 Z" fill="var(--accent-orange)"/></svg>Tennis / Golfers Elbow</li>
  </ul>

  <div class="footer-rule back-rule"></div>
  <div class="footer-band"></div>
  <div class="call-block call-footer">
    <svg class="phone-icon" viewBox="0 0 38 44" fill="none" stroke="var(--accent-orange)" stroke-width="2.2" stroke-linecap="round" stroke-linejoin="round">
      <path d="M8 6 L14 4 L18 15 L13 18 Q16 28 23 33 L28 29 L35 37 L30 41 Q16 42 8 26 Q3 14 8 6 Z"/>
      <path d="M22 9 Q28 11 29 18"/><path d="M23 3 Q33 6 35 17"/>
    </svg>
    <div>
      <div class="call-label">Visit Us Today</div>
      <div class="call-number">555.010.2040</div>
    </div>
  </div>
  <div class="brand-mark brand-footer back-footer-brand"><span class="brand-dot"></span><span>Brookmere Osteopathy</span></div>
</section>

</body>
</html>
```